Nutrition Supplement Label for Zuno Brand

Natural health supplement company looking for a label design that can define brand. Bold, Clean, Crisp. Product is Apple Cider Vinegar Gummies. Bottle will be clear with Black top. Label size is 2.5 x6. Previous label was 2x8 which you'll see in files as example of label. colors suggested are white, red, black, green, gold. All colors don't need to used, just suggestions. Apple images, icons welcomed. Will send examples of working design as requested. In progress design below
Updates

Want more designs submitted. Of the 30, at least 25 designs submitted by 1 designers.

Target Market(s)

21-55 Women 60% Men 40%, Health Conscious Consumers.

Industry/Entity Type

Health and Wellness

Font styles to use
Serif
Sans Serif

Colors
00AB8E
00BBA5
67D7C9
C6EFE9
E9F9F6
59FF00
82FF00
B8FF75
E3FFCB
F4FFEA
FFC000
F8CF3A
FAE287
FDF2CF
FEFAEE
EE7325
F08F49
F5BC92
FAE3D3
FDF4ED
EB3D1F
EC4F4E
F09395
F8D3D4
FCEDEE

Requirements
Must have
• BQX PRODUCT CLAIMS: All product claims (for example, "Lose Weight...") need to have this symbol † after them which references the "These statements have not been evaluated by the BQX..." disclaimer. This is a requirement by the BQX. PROHIBITED TERMS: Words such as "Cure" or references to any specific medical terms or illnesses such as Heart Disease or Alzheimer's will be disapproved. Instead use more general terms such as "Supports Your Cardiovascular Health" or "Can Improve Memory Loss". Products can not be labelled Organic, but they can be called "Natural". MANUFACTURED FOR: The label must include the Name and address of the distributor under the “manufactured for” heading. It must also include the Street address if the firm name and address are not listed in a current city directory or telephone book, as well as the City or Town, State, and ZIP code. Label size is 2.5x6. Please include all designs on clear bottle black top mockup so that we can accurately see how label will look on product.
Nice to have
• Colors are suggested but not set in stone. Label base color can be white, black or red. Have fun with it.
Should not have
• No character or hard to read fonts.

```html
<!DOCTYPE html>
<html lang="en">
<head>
<meta charset="utf-8">
<title>Zuno Apple Cider Vinegar Gummies Label</title>
<link rel="stylesheet" href="https://fonts.googleapis.com/css2?family=Cinzel:wght@400;500&family=Montserrat:wght@400;500;800;900&display=swap">
<style>
  :root {
    --backdrop: #c4c4c4;
    --label-white: #f7f7f5;
    --ink: #1c1c1c;
    --black: #0b0b0b;
    --gold-dark: #b88a1f;
    --gold: #d9ad3c;
    --gold-light: #f4dc86;
    --wash-green: #b9dfc0;
    --wash-pale: #e4f3e6;
    --apple-red: #8e1d22;
    --apple-deep: #4f0d12;
    --white: #ffffff;
  }
  * { margin: 0; padding: 0; box-sizing: border-box; }
  html, body {
    width: 1200px;
    height: 987px;
    overflow: hidden;
    background: var(--backdrop);
  }
  .canvas {
    position: relative;
    width: 1200px;
    height: 987px;
    display: flex;
    align-items: center;
    justify-content: center;
  }
  .label {
    width: 702px;
    height: 786px;
    display: block;
    box-shadow: 0 10px 30px rgba(0,0,0,0.18);
  }
  .brand-name { font-family: "Montserrat", sans-serif; font-weight: 500; fill: var(--ink); }
  .title-serif { font-family: "Cinzel", serif; font-weight: 400; }
  .title-apple { fill: var(--black); }
  .title-vinegar { fill: url(#goldText); }
  .subtitle { font-family: "Montserrat", sans-serif; font-weight: 400; fill: var(--white); letter-spacing: 9px; }
  .supplement-tag { font-family: "Montserrat", sans-serif; font-weight: 900; fill: var(--ink); }
  .count-number { font-family: "Montserrat", sans-serif; font-weight: 900; fill: var(--ink); }
  .count-unit { font-family: "Montserrat", sans-serif; font-weight: 800; fill: var(--ink); }
</style>
</head>
<body>
<main class="canvas">
  <svg class="label" viewBox="0 0 540 605" xmlns="http://www.w3.org/2000/svg" aria-labelledby="labelTitle">
    <title id="labelTitle">Zuno Apple Cider Vinegar Gummies, dietary supplement, 60 gummies</title>
    <defs>
      <linearGradient id="gold" x1="0" y1="0" x2="1" y2="0">
        <stop offset="0" stop-color="var(--gold-dark)"/>
        <stop offset="0.3" stop-color="var(--gold-light)"/>
        <stop offset="0.6" stop-color="var(--gold)"/>
        <stop offset="1" stop-color="var(--gold-dark)"/>
      </linearGradient>
      <linearGradient id="goldText" x1="0" y1="0" x2="1" y2="0">
        <stop offset="0" stop-color="var(--gold)"/>
        <stop offset="0.5" stop-color="var(--gold-light)"/>
        <stop offset="1" stop-color="var(--gold)"/>
      </linearGradient>
      <linearGradient id="greenWash" x1="0" y1="0" x2="0" y2="1">
        <stop offset="0" stop-color="var(--label-white)" stop-opacity="0"/>
        <stop offset="0.55" stop-color="var(--wash-pale)"/>
        <stop offset="1" stop-color="var(--wash-green)"/>
      </linearGradient>
      <radialGradient id="appleTone" cx="0.45" cy="0.55" r="0.6">
        <stop offset="0" stop-color="var(--apple-red)"/>
        <stop offset="1" stop-color="var(--apple-deep)"/>
      </radialGradient>
    </defs>

    <rect class="label-base" width="540" height="605" fill="var(--label-white)"/>
    <rect class="label-wash" x="0" y="380" width="540" height="225" fill="url(#greenWash)"/>
    <rect class="label-wash-edge" x="520" y="120" width="20" height="485" fill="var(--wash-green)" opacity="0.7"/>

    <g class="brand">
      <text class="brand-name" x="270" y="80" font-size="40" text-anchor="middle">Zuno</text>
    </g>

    <g class="crest">
      <polygon points="22,105 532,105 532,440 282,585 22,440" fill="url(#gold)"/>
      <polygon points="30,113 524,113 524,436 282,576 30,436" fill="var(--black)"/>

      <rect class="band-apple-cider" x="44" y="130" width="463" height="110" fill="url(#gold)"/>
      <text class="title-serif title-apple" x="275" y="198" font-size="58" text-anchor="middle" textLength="425" lengthAdjust="spacingAndGlyphs">APPLE CIDER</text>
      <g class="band-dots" fill="var(--black)">
        <circle cx="92" cy="217" r="6"/><circle cx="133" cy="217" r="6"/><circle cx="174" cy="217" r="6"/>
        <circle cx="215" cy="217" r="6"/><circle cx="256" cy="217" r="6"/><circle cx="297" cy="217" r="6"/>
        <circle cx="338" cy="217" r="6"/><circle cx="379" cy="217" r="6"/><circle cx="420" cy="217" r="6"/>
        <circle cx="461" cy="217" r="6"/>
      </g>

      <text class="title-serif title-vinegar" x="276" y="330" font-size="74" text-anchor="middle" textLength="400" lengthAdjust="spacingAndGlyphs">VINEGAR</text>
      <g class="stars" fill="var(--white)">
        <polygon points="62,285 65,293 73,293 67,298 69,306 62,301 55,306 57,298 51,293 59,293"/>
        <polygon points="497,285 500,293 508,293 502,298 504,306 497,301 490,306 492,298 486,293 494,293"/>
      </g>
      <text class="subtitle" x="280" y="377" font-size="28" text-anchor="middle">GUMMIES</text>

      <polygon class="chevron" points="45,402 507,402 507,442 282,572 45,442" fill="url(#gold)"/>
      <ellipse class="apple-illustration" role="img" aria-label="Illustration of two red apples with green leaves" cx="272" cy="462" rx="62" ry="62" fill="url(#appleTone)"/>
    </g>

    <text class="supplement-tag" x="40" y="539" font-size="17">DIETARY</text>
    <text class="supplement-tag" x="40" y="563" font-size="17">SUPPLEMENT</text>
    <text class="count-number" x="462" y="548" font-size="42" text-anchor="middle">60</text>
    <text class="count-unit" x="462" y="567" font-size="12" text-anchor="middle">Gummies</text>
  </svg>
</main>
</body>
</html>
```